Steadway Halvicor

We're designing a website to sell Halvicor Supplements. Attached is an image of the words we want to say and general layout, but please use your best knowledge to make it better. This platform is intentionally simplistic because this is reaching an older demographic, so it should be very straightforward, attention-grabbing and extremely user-friendly, while still appearing reliable and professional.
Use your best judgement for color palate that conveys professional but approachable. Feel free to add imagery but don't overwhelm the page.
Updates
Designs look the same
Target Market(s)
65+ seniors
Number of Pages Required
1 page
Look and feel

```html
<!DOCTYPE html>
<html lang="en">
<head>
<meta charset="utf-8">
<title>Steadway Halvicor</title>
<link rel="stylesheet" href="https://fonts.googleapis.com/css2?family=Open+Sans:wght@400;600;700;800&family=Lato:wght@400;700&family=Raleway:wght@300;400&display=swap">
<style>
:root{
  --navy:#0b3d6b;
  --heading:#155e8b;
  --blue:#1089c6;
  --page:#f7f7f7;
  --band:#f1f1f1;
  --card:#f0f0f0;
  --ink:#222;
  --body:#444;
  --muted:#555;
  --quote:#e1eaf2;
  --rule:#8fc3e0;
}
*{margin:0;padding:0;box-sizing:border-box}
html,body{width:1200px;height:2707px;overflow:hidden}
body{position:relative;background:var(--page);font-family:'Open Sans',sans-serif;color:var(--ink)}
.abs{position:absolute}

/* header */
.site-header{position:absolute;left:0;top:0;width:1200px;height:135px;background:var(--page)}
.brand{position:absolute;left:158px;top:52px;font-family:'Open Sans',sans-serif;font-weight:800;font-size:15px;line-height:16px;letter-spacing:2px;color:var(--navy)}
.nav a{position:absolute;top:63px;font-family:'Lato',sans-serif;font-size:17px;color:var(--navy);text-decoration:none}
.nav .active{color:#1e6b3a}
.nav-underline{position:absolute;left:327px;top:132px;width:74px;height:3px;background:#1e6b3a}
.call-pill{position:absolute;left:832px;top:42px;width:212px;height:50px;border-radius:25px;background:var(--navy);color:#fff;font-family:'Lato',sans-serif;font-weight:700;font-size:17px;display:flex;align-items:center;justify-content:center}

/* hero */
.hero{position:absolute;left:0;top:135px;width:1200px;height:625px;background:radial-gradient(ellipse at 85% 45%,#6b625a 0%,#3a3634 22%,#14161c 50%,#06080c 80%)}
.hero-wave{position:absolute;left:0;top:690px;width:1200px;height:75px}
.hero-title{position:absolute;left:203px;top:346px;font-size:40px;font-weight:700;letter-spacing:1px;color:#fff}
.hero-sub{position:absolute;left:204px;top:405px;font-family:'Raleway',sans-serif;font-size:25px;line-height:31px;color:#fff;letter-spacing:.4px}
.btn{position:absolute;height:59px;width:184px;border-radius:18px;display:flex;align-items:center;justify-content:center;font-size:11px;font-weight:700;color:#fff;letter-spacing:.3px}
.btn-solid{background:var(--blue)}
.btn-outline{border:1.5px solid var(--blue)}

/* why */
.section-title{position:absolute;font-size:30px;font-weight:700;color:var(--heading);letter-spacing:.5px}
.card{position:absolute;width:368px;height:300px;border-radius:48px;background:var(--card);text-align:center}
.card-art{position:absolute;left:126px;top:8px;width:116px;height:116px;border-radius:50%;background:linear-gradient(160deg,#d9d9d9,#c9ccce)}
.card h3{position:absolute;left:0;right:0;top:144px;font-size:19px;font-weight:600;letter-spacing:.6px;color:#111}
.card p{position:absolute;left:28px;right:28px;top:196px;font-family:'Lato',sans-serif;font-size:11.5px;line-height:21px;color:var(--body)}

/* testimonials */
.band{position:absolute;left:0;top:1582px;width:1200px;height:545px}
.quote-mark{position:absolute;font-family:'Open Sans',sans-serif;font-weight:800;font-size:190px;line-height:1;color:var(--quote)}
.avatar{position:absolute;width:75px;height:75px;border-radius:50%;background:linear-gradient(150deg,#b8b2aa,#5e5a56)}
.avatar-active{width:92px;height:92px;border:4px solid var(--blue);box-shadow:inset 0 0 0 4px var(--band)}
.testimonial{position:absolute;left:558px;top:1907px;width:440px;text-align:center;font-family:'Lato',sans-serif;font-size:11.5px;line-height:21px;color:#222}
.attribution{position:absolute;left:760px;top:2067px;width:211px;text-align:right;font-family:'Lato',sans-serif;font-size:12px;font-weight:700;color:#222}

/* cta */
.cta{position:absolute;left:0;top:2121px;width:1200px;height:285px;background:linear-gradient(180deg,#3f5c62 0%,#2a3a40 45%,#141c22 100%);overflow:hidden}
.cta-shape{position:absolute;left:605px;top:0;width:700px;height:560px;border-radius:50%;background:rgba(60,70,76,.55)}
.cta-title{position:absolute;left:710px;top:2184px;font-size:32px;font-weight:700;letter-spacing:5px;color:#fff}
.cta-sub{position:absolute;left:711px;top:2233px;font-family:'Raleway',sans-serif;font-size:17px;color:#fff;letter-spacing:.3px}

/* footer */
.footer-brand{position:absolute;left:158px;top:2498px;font-weight:800;font-size:27px;line-height:28px;letter-spacing:3px;color:var(--navy)}
.f-head{position:absolute;top:2455px;font-family:'Lato',sans-serif;font-size:12px;color:#222;letter-spacing:.3px}
.f-link{position:absolute;left:425px;font-family:'Raleway',sans-serif;font-size:10px;color:var(--muted)}
.f-text{position:absolute;left:623px;font-family:'Raleway',sans-serif;font-size:10px;line-height:21px;color:var(--muted)}
.f-icon{position:absolute;left:595px}
.social{position:absolute;top:2482px;width:18px;height:18px;border-radius:50%;background:#222}
.footer-rule{position:absolute;left:150px;top:2648px;width:900px;height:2px;background:var(--rule)}
.legal{position:absolute;top:2672px;font-family:'Raleway',sans-serif;font-size:10px;color:#333}
</style>
</head>
<body>

<header class="site-header">
  <div class="brand">STEADWAY<br>HALVICOR</div>
  <nav class="nav">
    <a class="active" style="left:337px">HOME</a>
    <a style="left:481px">SERVICES</a>
    <a style="left:653px">GET QUOTE</a>
  </nav>
  <div class="nav-underline"></div>
  <div class="call-pill">CALL - (800) 555-0148</div>
</header>

<section class="hero" role="img" aria-label="Photo of an elderly woman with glasses in profile against a dark background"></section>
<svg class="hero-wave" viewBox="0 0 1200 75" preserveAspectRatio="none" aria-hidden="true">
  <path d="M0 46 C90 30 170 14 242 14 C420 14 680 72 946 67 C1060 65 1140 50 1200 46 L1200 75 L0 75 Z" fill="#f7f7f7"/>
</svg>
<h1 class="hero-title">STEADWAY HALVICOR</h1>
<p class="hero-sub">Be confident choosing the Halvicor<br>Supplement plan that's right for you</p>
<div class="btn btn-solid" style="left:226px;top:512px">ENTER ZIP CODE</div>
<div class="btn btn-outline" style="left:437px;top:512px">CALL NOW</div>

<h2 class="section-title" style="left:203px;top:800px">WHY CHOOSE US</h2>

<div class="card" style="left:160px;top:914px">
  <div class="card-art" role="img" aria-label="Illustration of a laptop with a clock"></div>
  <h3>SAVE TIME</h3>
  <p>Lorem ipsum dolor sit amet, consectetur adipisicing elit, sed do eiusmod tempor incididunt ut labore et dolore magna aliqua.</p>
</div>
<div class="card" style="left:673px;top:914px">
  <div class="card-art" role="img" aria-label="Illustration of a doctor on a screen with a speech bubble"></div>
  <h3>PLAN RECOMMENDATION</h3>
  <p>Ut enim ad minim veniam, quis nostrud exercitation ullamco laboris nisi ut aliquip ex ea commodo consequat.</p>
</div>
<div class="card" style="left:160px;top:1291px">
  <div class="card-art" role="img" aria-label="Illustration of a video call window with a person"></div>
  <h3>TALK TO EXPERT</h3>
  <p>Duis aute irure dolor in reprehenderit in voluptate velit esse cillum dolore eu fugiat nulla pariatur.</p>
</div>
<div class="card" style="left:673px;top:1291px">
  <div class="card-art" role="img" aria-label="Illustration of a document with a banknote"></div>
  <h3>SAVE MONEY</h3>
  <p>Sed ut perspiciatis unde omnis iste natus error sit voluptatem accusantium doloremque laudantium, totam rem aperiam, eaque ipsa quae ab illo inventore veritatis et quasi architecto beatae explicabo.</p>
</div>

<svg class="band" viewBox="0 0 1200 545" preserveAspectRatio="none" aria-hidden="true">
  <path d="M0 0 L1200 84 L1200 545 L0 545 Z" fill="#f1f1f1"/>
</svg>

<h2 class="section-title" style="left:202px;top:1732px">TESTIMONIALS</h2>
<div class="quote-mark" style="left:488px;top:1722px">&ldquo;</div>
<div class="quote-mark" style="left:960px;top:1968px">&rdquo;</div>

<div class="avatar avatar-active" style="left:289px;top:1799px" role="img" aria-label="Portrait of an elderly woman, selected"></div>
<div class="avatar" style="left:396px;top:1808px" role="img" aria-label="Portrait of an elderly woman smiling"></div>
<div class="avatar" style="left:191px;top:1907px" role="img" aria-label="Portrait of an elderly man in a hat"></div>
<div class="avatar" style="left:294px;top:1907px" role="img" aria-label="Portrait of a woman with dark hair"></div>
<div class="avatar" style="left:399px;top:1907px" role="img" aria-label="Portrait of a man in black and white"></div>
<div class="avatar" style="left:191px;top:2005px" role="img" aria-label="Portrait of an elderly woman in black and white"></div>
<div class="avatar" style="left:305px;top:2005px" role="img" aria-label="Portrait of an elderly man with glasses"></div>

<svg class="abs" style="left:156px;top:1887px" width="16" height="22" viewBox="0 0 16 22" aria-label="Previous"><path d="M13 2 L3 11 L13 20" fill="none" stroke="#155e8b" stroke-width="2"/></svg>
<svg class="abs" style="left:1027px;top:1887px" width="16" height="22" viewBox="0 0 16 22" aria-label="Next"><path d="M3 2 L13 11 L3 20" fill="none" stroke="#155e8b" stroke-width="2"/></svg>

<p class="testimonial">Nemo enim ipsam voluptatem quia voluptas sit aspernatur aut odit aut fugit, sed quia consequuntur magni dolores eos qui ratione voluptatem sequi nesciunt. Neque porro quisquam est, qui dolorem ipsum quia dolor sit amet, consectetur, adipisci velit.</p>
<p class="attribution">- Marian (66 years old)</p>

<section class="cta" role="img" aria-label="Photo of an elderly man looking out over the sea">
  <div class="cta-shape"></div>
</section>
<h2 class="cta-title">GET STARTED NOW</h2>
<p class="cta-sub">Lorem ipsum dolor sit amet, consectetur</p>
<div class="btn btn-solid" style="left:696px;top:2289px">ENTER ZIP CODE</div>
<div class="btn btn-outline" style="left:907px;top:2289px">CALL NOW</div>

<footer>
  <div class="footer-brand">STEADWAY<br>HALVICOR</div>

  <div class="f-head" style="left:425px">QUICK LINKS</div>
  <div class="f-link" style="top:2481px">HOME</div>
  <div class="f-link" style="top:2502px">SERVICES</div>
  <div class="f-link" style="top:2523px">CONTACT</div>
  <div class="f-link" style="top:2544px">QUOTE</div>

  <div class="f-head" style="left:595px">CONTACT US</div>
  <svg class="f-icon" style="top:2482px" width="17" height="19" viewBox="0 0 17 19" aria-label="Address"><path d="M8.5 1 C5 1 3 3.5 3 6.3 C3 9.8 8.5 15 8.5 15 C8.5 15 14 9.8 14 6.3 C14 3.5 12 1 8.5 1 Z" fill="none" stroke="#1089c6" stroke-width="1.6"/><circle cx="8.5" cy="6.3" r="2" fill="#1089c6"/><path d="M1 18 L16 18" stroke="#0b3d6b" stroke-width="1.4"/></svg>
  <div class="f-text" style="top:2481px">12 ORCHARD LANE, FAIRBROOK,<br>WESTLAND</div>
  <svg class="f-icon" style="top:2532px" width="17" height="12" viewBox="0 0 17 12" aria-label="Email"><rect x="0.7" y="0.7" width="15.6" height="10.6" fill="none" stroke="#222" stroke-width="1.3"/><path d="M1 1 L8.5 7 L16 1" fill="none" stroke="#222" stroke-width="1.3"/></svg>
  <div class="f-text" style="top:2527px">HELLO@STEADWAYMAIL.COM</div>
  <svg class="f-icon" style="left:597px;top:2560px" width="12" height="18" viewBox="0 0 12 18" aria-label="Phone"><rect x="0.8" y="0.8" width="10.4" height="16.4" rx="1.5" fill="none" stroke="#222" stroke-width="1.5"/><rect x="3.5" y="14" width="5" height="1.3" fill="#222"/></svg>
  <div class="f-text" style="top:2559px">(800) 555-0148</div>

  <div class="f-head" style="left:864px">STAY CONNECTED</div>
  <div class="social" style="left:864px" aria-label="Social link"></div>
  <div class="social" style="left:890px" aria-label="Social link"></div>
  <div class="social" style="left:915px" aria-label="Social link"></div>
  <div class="social" style="left:940px" aria-label="Social link"></div>
  <div class="social" style="left:966px" aria-label="Social link"></div>

  <div class="footer-rule"></div>
  <div class="legal" style="left:152px">&copy;2020 STEADWAY HALVICOR ALL RIGHTS RESERVED</div>
  <div class="legal" style="left:752px">PRIVACY POLICY</div>
  <div class="legal" style="left:874px">|</div>
  <div class="legal" style="left:910px">TERMS AND CONDITIONS</div>
</footer>

</body>
</html>
```